Business card design for Automotive workshop

We need a business card for a new automotive repair and tyre shop called Ridgeback Prime Automotive located in New Zealand. We are a clean, modern and fresh workshop and company.

Front needs to feature logo,
my name:
Lachie Westergaard (director)

Address:
48 Marlow Lane
Whitianga 3510

Phone: 07 842 1937
Mobile: 027 519 2764
Email: office@ridgebackmotors.co.nz
Website: ridgebackmotors.co.nz

Back needs to feature an area to write down appointment details, date and time.

Also feature a list of jobs and work we do such as,
Vehicle Servicing
All Mechanical Repairs
Warrant of Fitness
Tyres & Wheel Alignments
Automotive Diagnostics
Automotive Parts & Supplies

```html
<!DOCTYPE html>
<html lang="en">
<head>
<meta charset="utf-8">
<title>Ridgeback Prime Automotive – Business Card</title>
<link rel="stylesheet" href="https://fonts.googleapis.com/css2?family=Montserrat:wght@500;600;800&display=swap">
<style>
  :root {
    --page-bg: #e4e4e4;
    --card-dark: #161616;
    --card-light: #f3f3f3;
    --brand-red: #d71f26;
    --ink-white: #f2f2f2;
    --ink-soft: #bdbdbd;
    --ink-black: #141414;
    --rule-grey: #8a8a8a;
    --divider-grey: #5a5a5a;
  }
  * { box-sizing: border-box; margin: 0; padding: 0; }
  html, body {
    width: 1200px; height: 900px; overflow: hidden;
    background: var(--page-bg);
    font-family: "Montserrat", Arial, sans-serif;
  }
  .card {
    position: absolute; left: 353px;
    width: 490px; height: 317px;
    box-shadow: 0 6px 14px rgba(0,0,0,0.25);
  }
  .card-front { top: 93px; background: var(--card-dark); }
  .card-back  { top: 457px; background: var(--card-light); }

  .brand-name {
    position: absolute; left: 0; right: 0;
    text-align: center; color: var(--brand-red);
    font-weight: 800; text-transform: uppercase; line-height: 1;
  }
  .brand-name .line-main { display: block; font-size: 42px; letter-spacing: 1px; }
  .brand-name .line-sub  { display: block; font-size: 17px; letter-spacing: 9px; margin-top: 8px; padding-left: 9px; }
  .card-front .brand-name { top: 40px; }
  .card-back .brand-name  { top: 52px; }
  .card-back .brand-name .line-main { font-size: 36px; }
  .card-back .brand-name .line-sub  { font-size: 15px; letter-spacing: 8px; }

  .person {
    position: absolute; right: 228px; top: 172px;
    text-align: right; color: var(--ink-white);
  }
  .person-name { color: var(--brand-red); font-weight: 600; font-size: 21px; letter-spacing: 1.5px; line-height: 1.1; }
  .person-role { font-weight: 600; font-size: 9px; letter-spacing: 1px; margin-top: 6px; }
  .person-address { font-weight: 500; font-size: 9px; letter-spacing: 0.8px; line-height: 18px; margin-top: 8px; }

  .divider {
    position: absolute; left: 273px; top: 170px;
    width: 1px; height: 94px; background: var(--divider-grey);
  }
  .contact-list {
    position: absolute; left: 282px; top: 176px; list-style: none;
    color: var(--ink-white);
  }
  .contact-list li {
    display: flex; align-items: center; height: 21px;
    font-weight: 500; font-size: 9px; letter-spacing: 0.4px;
  }
  .contact-list svg { width: 16px; height: 16px; margin-right: 13px; flex: none; }

  .service-list {
    position: absolute; left: 30px; right: 30px; top: 279px;
    list-style: none; display: flex; flex-wrap: wrap; justify-content: center;
    row-gap: 4px; color: var(--ink-soft);
    font-weight: 500; font-size: 8px; letter-spacing: 0.5px; line-height: 11px;
  }
  .service-list li { padding: 0 7px; position: relative; }
  .service-list li + li::before {
    content: ""; position: absolute; left: -2px; top: 4px;
    width: 3px; height: 3px; background: var(--brand-red);
  }
  .service-list li:nth-child(4)::before { display: none; }
  .service-list .row-break { flex-basis: 100%; height: 0; padding: 0; }

  .appointment {
    position: absolute; left: 97px; top: 155px; width: 296px;
  }
  .appointment-field {
    border-top: 1px solid var(--rule-grey);
    height: 49px; padding-top: 6px;
    text-align: center; color: var(--ink-black);
    font-weight: 600; font-size: 13px;
  }
</style>
</head>
<body>

<section class="card card-front" aria-label="Business card front">
  <h1 class="brand-name">
    <span class="line-main">Ridgeback Prime</span>
    <span class="line-sub">Automotive</span>
  </h1>

  <div class="person">
    <p class="person-name">Lachie Westergaard</p>
    <p class="person-role">DIRECTOR</p>
    <p class="person-address">48 Marlow Lane<br>Whitianga 3510</p>
  </div>

  <div class="divider"></div>

  <ul class="contact-list">
    <li>
      <svg viewBox="0 0 24 24" aria-hidden="true"><path fill="#d71f26" d="M6.6 10.8a15.1 15.1 0 0 0 6.6 6.6l2.2-2.2a1 1 0 0 1 1-.25 11.4 11.4 0 0 0 3.6.57 1 1 0 0 1 1 1V20a1 1 0 0 1-1 1A17 17 0 0 1 3 4a1 1 0 0 1 1-1h3.5a1 1 0 0 1 1 1c0 1.25.2 2.45.57 3.57a1 1 0 0 1-.25 1z"/></svg>
      07 842 1937
    </li>
    <li>
      <svg viewBox="0 0 24 24" aria-hidden="true"><rect x="6.5" y="2" width="11" height="20" rx="2" fill="none" stroke="#d71f26" stroke-width="2"/><circle cx="12" cy="18.5" r="1.2" fill="#d71f26"/></svg>
      027 519 2764
    </li>
    <li>
      <svg viewBox="0 0 24 24" aria-hidden="true"><path fill="#d71f26" d="M3 6h18v12H3z"/><path fill="none" stroke="#161616" stroke-width="1.6" d="M3 6l9 7 9-7"/></svg>
      office@ridgebackmotors.co.nz
    </li>
    <li>
      <svg viewBox="0 0 24 24" aria-hidden="true"><g fill="none" stroke="#d71f26" stroke-width="1.6"><circle cx="12" cy="12" r="9"/><ellipse cx="12" cy="12" rx="4" ry="9"/><path d="M3 12h18M4.5 7.5h15M4.5 16.5h15"/></g></svg>
      ridgebackmotors.co.nz
    </li>
  </ul>

  <ul class="service-list" aria-label="Services">
    <li>Vehicle Servicing</li>
    <li>All Mechanical Repairs</li>
    <li>Warrant of Fitness</li>
    <li class="row-break" aria-hidden="true"></li>
    <li>Tyres &amp; Wheel Alignments</li>
    <li>Automotive Diagnostics</li>
    <li>Automotive Parts &amp; Supplies</li>
  </ul>
</section>

<section class="card card-back" aria-label="Business card back">
  <h2 class="brand-name">
    <span class="line-main">Ridgeback Prime</span>
    <span class="line-sub">Automotive</span>
  </h2>

  <div class="appointment">
    <p class="appointment-field">Appointment Details</p>
    <p class="appointment-field">Date</p>
    <p class="appointment-field">Time</p>
  </div>
</section>

</body>
</html>
```